Camp Thornbrook 2021 Magazine Design

We are for someone to design our annual magazine/newsletter. This is a print newsletter that is a total of 20 pages. It will need to be designed in a way that is easy to share with our printers. The designer will need to be someone who is creative and easy to work with.
For those interested in this project we ask that you design 4 to 6 pages for us to view. Once we select the designer we will want the rest created in a two-week time span. For those submitting a bid please include front cover, theme & dates, mission & vision, and Make the Difference.

This link will provide the layout of the newsletter https://files.pelmarcloud.example/doc/7qzRt2LmXv9KpWnD4sHy8bCe3FaJu6NgQo5/edit?usp=sharing.

This link will provide you with the pictures that are needed and a few documents https://files.pelmarcloud.example/folders/5TbQx8WnLr2VkYcPz3HmDs7?usp=sharing

Details:
20 pages long (including covers)
8.5 x 11

Please message me if you need any further details.

Target Market(s)

Our alumni base. Covers all ages

Requirements
Must have
• Spelled out in document
Nice to have
• Spelled out in document
Should not have
• Spelled out in document

```html
<!DOCTYPE html>
<html lang="en">
<head>
<meta charset="utf-8">
<title>Camp Thornbrook – Sessions, Ages and Activities</title>
<link rel="stylesheet" href="https://fonts.googleapis.com/css2?family=Bebas+Neue&family=Noto+Serif:wght@400&display=swap">
<style>
:root{
  --slate:#6a6a7e;
  --grey-bar:#8a8d8f;
  --row:#e6e6e7;
  --row-line:#d2d2d4;
  --ink:#1e1e1e;
  --gold:#ffc857;
  --gold-soft:#fde3b0;
  --rose:#f4939a;
  --rose-soft:#fbd6d8;
  --orange:#f26b2b;
  --teal:#8fd4c6;
  --paper:#ffffff;
}
*{margin:0;padding:0;box-sizing:border-box}
html,body{width:927px;height:1200px;overflow:hidden;background:var(--paper)}
.page{position:relative;width:927px;height:1200px;overflow:hidden;font-family:"Noto Serif",serif;color:var(--ink)}
.backdrop-left{position:absolute;left:0;top:0;width:412px;height:440px;background:linear-gradient(100deg,#e9eaeb 0%,#b8babc 100%)}
.backdrop-left::after{content:"";position:absolute;inset:0;background:linear-gradient(180deg,rgba(255,255,255,0) 55%,#fff 100%)}
.backdrop-right{position:absolute;left:412px;top:0;width:515px;height:505px;background:linear-gradient(180deg,var(--slate) 0%,#7a7a8c 55%,#d8d8de 85%,#ffffff 100%)}
.wave-art{position:absolute;left:590px;top:80px;width:337px;height:320px;border-radius:50% 0 0 50%;background:linear-gradient(120deg,rgba(244,147,154,.45) 0%,rgba(240,170,140,.55) 45%,rgba(250,200,120,.45) 75%,rgba(220,160,200,.4) 100%)}
.label-bar{position:absolute;left:0;height:27px;font-family:"Bebas Neue",sans-serif;color:#fff;font-size:21px;line-height:29px;letter-spacing:.3px}
.label-sessions{top:108px;width:265px;background:var(--grey-bar);padding-left:84px;height:35px;line-height:37px}
.label-activities{top:664px;width:230px;background:var(--orange);padding-left:64px}
.sessions{position:absolute;left:0;top:146px;width:589px}
.session-row{display:flex;height:24px;margin-bottom:5px;font-size:14.5px;line-height:25px}
.session-row span{background:var(--row);border-bottom:1px solid var(--row-line)}
.s-name{width:234px;padding-left:84px}
.s-dates{width:177px;padding-left:13px;background:#ececed!important}
.s-price{width:178px;padding-left:55px;background:#f1f1f2!important}
.age-table{position:absolute;top:491px;width:0}
.cell{position:absolute;left:0;height:23px;font-size:14.5px;line-height:24px;padding-left:21px}
.head{font-family:"Bebas Neue",sans-serif;font-size:21px;line-height:26px}
.groups{left:63px}.groups .cell{width:108px;background:var(--gold-soft)}.groups .head{background:var(--gold)}
.ages{left:230px}.ages .cell{width:120px;background:var(--rose-soft);padding-left:17px}.ages .head{background:var(--rose)}
.camp-photo{position:absolute;left:390px;top:489px;width:234px;height:143px;background:linear-gradient(180deg,#dfe8ee 0%,#a9c38a 45%,#5f8a3e 75%,#8f8a7a 100%)}
.activity{position:absolute;display:flex;align-items:center;font-size:16px;height:60px;white-space:nowrap}
.activity .icon{width:60px;height:60px;border-radius:50%;border:1.5px solid #111;flex:none;margin-right:16px}
.icon.empty{background:#fff}
.a1{background:linear-gradient(135deg,#7aa858,#2f4a2a)}
.a2{background:linear-gradient(135deg,#9fc3dc,#3a6e8c 60%,#e8c840)}
.a3{background:linear-gradient(135deg,#c8d4de,#7a5a3a 60%,#6c8a50)}
.a4{background:linear-gradient(135deg,#c7dcef,#7a8c9a 60%,#4a4a4a)}
.a5{background:linear-gradient(135deg,#e8c040,#8a6a20 60%,#3a5a2a)}
.a6{background:linear-gradient(135deg,#a8cce8,#d8c8b0 60%,#6a8a9a)}
.a7{background:linear-gradient(135deg,#6a8a4a,#c8d4a8 60%,#3a5a3a)}
.a8{background:linear-gradient(135deg,#111,#3a2a1a 60%,#d86a20)}
.a9{background:linear-gradient(135deg,#d85a8a,#5a7ad8 50%,#f0c8c0)}
.a10{background:linear-gradient(135deg,#dce4ec,#8a9aa8 60%,#6a7a5a)}
.a11{background:linear-gradient(135deg,#9ad0e8,#2a6a9a 60%,#e0f0f8)}
.page-number{position:absolute;left:891px;top:1152px;width:18px;height:24px;background:var(--teal);font-family:"Bebas Neue",sans-serif;font-size:16px;line-height:27px;text-align:center}
.footer-band{position:absolute;left:0;top:1176px;width:927px;height:24px;background:var(--teal)}
</style>
</head>
<body>
<div class="page">
  <div class="backdrop-left"></div>
  <div class="backdrop-right"></div>
  <div class="wave-art" role="img" aria-label="Decorative flowing line waves and angled stripes in coral, peach and lilac"></div>

  <div class="label-bar label-sessions">Sessions and Dates</div>
  <div class="sessions">
    <div class="session-row"><span class="s-name">Session 1</span><span class="s-dates">May 30 - June 5</span><span class="s-price">($285)</span></div>
    <div class="session-row"><span class="s-name">Short Session 1</span><span class="s-dates">May 30 - June 2</span><span class="s-price">($175)</span></div>
    <div class="session-row"><span class="s-name">Session 2</span><span class="s-dates">June 6 - June 17</span><span class="s-price">($425)</span></div>
    <div class="session-row"><span class="s-name">Session 2B</span><span class="s-dates">June 6 - June 12</span><span class="s-price">($285)</span></div>
    <div class="session-row"><span class="s-name">Session 3</span><span class="s-dates">June 27 - July 8</span><span class="s-price">($425)</span></div>
    <div class="session-row"><span class="s-name">Session 3B</span><span class="s-dates">June 27 - July 3</span><span class="s-price">($285)</span></div>
    <div class="session-row"><span class="s-name">Session 4</span><span class="s-dates">July 11 - July 22</span><span class="s-price">($425)</span></div>
    <div class="session-row"><span class="s-name">Session 4B</span><span class="s-dates">July 11 - July 17</span><span class="s-price">($285)</span></div>
    <div class="session-row"><span class="s-name">Session 5</span><span class="s-dates">July 25 - July 31</span><span class="s-price">($285)</span></div>
    <div class="session-row"><span class="s-name">Short Session 2</span><span class="s-dates">July 25 - July 28</span><span class="s-price">($175)</span></div>
  </div>

  <div class="age-table groups">
    <div class="cell head" style="top:0">Group</div>
    <div class="cell" style="top:30px">1</div>
    <div class="cell" style="top:59px">2</div>
    <div class="cell" style="top:88px">3</div>
    <div class="cell" style="top:117px">4</div>
  </div>
  <div class="age-table ages">
    <div class="cell head" style="top:0">Age</div>
    <div class="cell" style="top:30px">8-10 Years</div>
    <div class="cell" style="top:59px">11-12 Years</div>
    <div class="cell" style="top:88px">13-14 Years</div>
    <div class="cell" style="top:117px">15-18 Years</div>
  </div>
  <div class="camp-photo" role="img" aria-label="Photo of two campers in green shirts seen from behind, looking at the camp entrance gate among trees"></div>

  <div class="label-bar label-activities">Activities</div>

  <div class="activity" style="left:70px;top:714px"><div class="icon a1" role="img" aria-label="Foam-tip arrow game photo"></div>Arrow Dodge</div>
  <div class="activity" style="left:340px;top:714px"><div class="icon a2" role="img" aria-label="Lake blob photo"></div>Blob</div>
  <div class="activity" style="left:609px;top:714px"><div class="icon a3" role="img" aria-label="Horseback riding photo"></div>Horseback Riding</div>

  <div class="activity" style="left:70px;top:797px"><div class="icon a4" role="img" aria-label="Hiking photo"></div>Hiking</div>
  <div class="activity" style="left:340px;top:797px"><div class="icon a5" role="img" aria-label="Gaga ball pit photo"></div>Gaga Ball</div>
  <div class="activity" style="left:609px;top:797px"><div class="icon empty"></div>Golden Goal (New)</div>

  <div class="activity" style="left:70px;top:883px"><div class="icon a6" role="img" aria-label="Rappelling photo"></div>Rappelling</div>
  <div class="activity" style="left:340px;top:883px"><div class="icon a7" role="img" aria-label="Archery photo"></div>Archery</div>
  <div class="activity" style="left:609px;top:883px"><div class="icon empty"></div>Hatchet Throwing (New)</div>

  <div class="activity" style="left:70px;top:970px"><div class="icon a8" role="img" aria-label="Basketball hoop photo"></div>Basketball</div>
  <div class="activity" style="left:340px;top:970px"><div class="icon a9" role="img" aria-label="Arts and crafts supplies photo"></div>Arts and Crafts</div>
  <div class="activity" style="left:609px;top:970px"><div class="icon a10" role="img" aria-label="Overhead grid volley game photo"></div>Sky Grid Volley</div>

  <div class="activity" style="left:70px;top:1057px"><div class="icon a11" role="img" aria-label="Swimming photo"></div>Swimming</div>
  <div class="activity" style="left:340px;top:1057px"><div class="icon empty"></div>And much more!</div>

  <div class="page-number">7</div>
  <div class="footer-band"></div>
</div>
</body>
</html>
```